Where Quiet Waters Bend

I have a previously designed book cover, and although I am mostly happy with it, I do not care for the photo on the cover of the book. I would like to keep the fonts and scrollwork on the current book cover (the brown outer edge is optional).
I prefer a Christian focus with a soft, gentle, grieving, trusting feeling of a mother as God leads without the typical religious symbols (ie: huge hands, overwhelming crosses, Heaven opening). Softly toned or small Christian icons would be acceptable.
The book dimensions are 5.5 X 8.5 and the spine is 1/2" thick.
Original book cover is here: http://wherequietwatersbend.pagenookhost.net/p/free-books.html
Back cover book description (two photos and the logo for the back cover can be found below) :
For I am the Lord your God who takes hold of your right hand and says to you, "Do not fear, I will help you." Isaiah 41:13
One day you were here, Colby, the next you were at the throne of God. How I long to know what heaven is like so I can envision where you are. Are you talking to Gideon about the battles of old? Are you asking Paul about the stonings, the scales, and the shipwrecks? Or are you still just standing in awe of the God and Savior that your mother could never have come close to describing to you? How I long to stand in awe with you, praising the God who gives and takes away. Just like I told you all those times when you were here with us, "If you go first, I'll see you when I get there, my son." Love you, Mom
On Friday, February 18, 2011, God did the unthinkable in our lives: He chose to take our 12-year-old son, Colby, home to heaven in a skiing accident. It is only considered the unthinkable because our plans are not God's plans and our ways are not God's ways. Follow along on my journey through the valley of the shadow of death as my Savior, Jesus Christ, leads me.
(Author info)
Janna L. Brockwood lives on a small farm in northern Wisconsin with her husband, Dale, and their children. Experiencing the tragic death of her son has caused her to draw closer to God as He leads her down an unexpected path to know Him better.
I have updated the back cover details to include the exact words for the back cover as well as two photos and a logo. Thank you, designers, for sharing your creativity!
Reason: Still looking for the perfect book cover!
Reason: Still looking for the perfect design!
Working on final revisions!

```html
<!DOCTYPE html>
<html lang="en">
<head>
<meta charset="utf-8">
<title>Where Quiet Waters Bend – Book Cover</title>
<link rel="stylesheet" href="https://fonts.googleapis.com/css2?family=Cinzel:wght@400;500&family=Tinos:wght@400&display=swap">
<style>
  :root {
    --sky-top: #2f8ea6;
    --sky-mid: #6cc0cf;
    --sky-light: #d6eef0;
    --horizon: #c9d6cf;
    --field-gold: #a08a52;
    --field-brown: #5e4a30;
    --field-dark: #2e2418;
    --ink: #1d1d1b;
    --white: #ffffff;
    --spine-shade: rgba(20, 40, 45, 0.18);
    --portrait-a: #9a8a78;
    --portrait-b: #c9b7a4;
    --press-gold: #d9b25a;
  }
  * { margin: 0; padding: 0; box-sizing: border-box; }
  html, body { width: 1200px; height: 889px; overflow: hidden; background: #fff; }
  .cover-wrap {
    position: relative;
    width: 1200px;
    height: 889px;
    overflow: hidden;
    font-family: "Tinos", "Times New Roman", serif;
  }
  .scene {
    position: absolute; inset: 0;
    background:
      radial-gradient(ellipse 420px 260px at 900px 420px, rgba(255,255,255,0.55), rgba(255,255,255,0) 70%),
      radial-gradient(ellipse 360px 200px at 260px 420px, rgba(255,255,255,0.45), rgba(255,255,255,0) 70%),
      linear-gradient(180deg, var(--sky-top) 0%, var(--sky-mid) 32%, var(--sky-light) 55%, var(--horizon) 59.5%, var(--field-gold) 62%, var(--field-brown) 80%, var(--field-dark) 100%);
  }
  .spine-band {
    position: absolute; top: 0; bottom: 0; left: 570px; width: 56px;
    background: var(--spine-shade);
  }

  /* Back cover */
  .back-title {
    position: absolute; left: 0; width: 575px; top: 92px;
    text-align: center; color: var(--ink);
    font-family: "Cinzel", serif; line-height: 1;
  }
  .back-title .big { display: block; font-size: 44px; letter-spacing: 1px; }
  .back-title .small {
    display: flex; align-items: center; justify-content: center; gap: 8px;
    font-size: 13px; margin: 3px 0 4px;
  }
  .back-title .small::before, .back-title .small::after {
    content: ""; width: 32px; height: 1px; background: var(--ink);
  }
  .back-copy {
    position: absolute; left: 58px; top: 222px; width: 490px;
    font-size: 13.4px; line-height: 16px; color: var(--ink);
  }
  .back-copy p + p { margin-top: 16px; }
  .portrait {
    position: absolute; top: 697px; width: 70px; height: 70px; border-radius: 50%;
    background: radial-gradient(circle at 50% 40%, var(--portrait-b), var(--portrait-a));
    border: 2px solid rgba(255,255,255,0.7);
  }
  .portrait.author { left: 38px; }
  .portrait.child { left: 458px; }
  .author-bio {
    position: absolute; left: 127px; top: 703px; width: 326px;
    font-size: 11px; line-height: 14px; color: var(--white);
  }
  .press-mark {
    position: absolute; left: 236px; top: 790px; width: 104px;
    display: flex; align-items: center; gap: 6px;
    font-family: "Tinos", serif; font-size: 12px; line-height: 14px;
    color: var(--press-gold); text-transform: uppercase;
  }
  .press-mark::before {
    content: ""; flex: none; width: 10px; height: 10px; background: var(--press-gold);
  }

  /* Spine */
  .spine-title {
    position: absolute; left: 598px; top: 440px;
    transform: translate(-50%, -50%) rotate(90deg);
    white-space: nowrap; font-family: "Cinzel", serif;
    font-size: 27px; letter-spacing: 1px; color: var(--ink);
  }
  .spine-press {
    position: absolute; left: 598px; top: 775px;
    transform: translate(-50%, -50%) rotate(90deg);
    display: flex; align-items: center; gap: 5px; white-space: nowrap;
    font-size: 9px; color: var(--press-gold); text-transform: uppercase;
  }
  .spine-press::before { content: ""; width: 7px; height: 7px; background: var(--press-gold); }

  /* Front cover */
  .front-verse {
    position: absolute; left: 640px; width: 545px; top: 22px;
    text-align: center; color: var(--white);
    font-family: "Cinzel", serif; font-size: 11.5px; line-height: 17px;
  }
  .front-title {
    position: absolute; left: 626px; width: 574px; top: 110px;
    text-align: center; color: var(--ink);
    font-family: "Cinzel", serif; line-height: 0.9;
  }
  .front-title .big { display: block; font-size: 104px; }
  .front-title .big.last { font-size: 80px; }
  .front-title .small {
    display: flex; align-items: center; justify-content: center; gap: 14px;
    font-size: 30px; margin: 8px 0 6px;
  }
  .front-title .small::before, .front-title .small::after {
    content: ""; width: 76px; height: 2px; background: var(--ink);
  }
  .front-author {
    position: absolute; left: 626px; width: 574px; top: 795px;
    text-align: center; color: var(--white);
    font-family: "Cinzel", serif; font-size: 29px; letter-spacing: 0.5px;
  }
</style>
</head>
<body>
<main class="cover-wrap">
  <div class="scene" role="img" aria-label="Photograph of a soft teal sky with drifting clouds above golden wheat fields, a young man walking away down a dirt farm road toward the horizon, with a pair of open hands faint in the clouds on the front"></div>
  <div class="spine-band"></div>

  <section class="back-cover">
    <h2 class="back-title">
      <span class="big">WHERE</span>
      <span class="small">QUIET WATERS</span>
      <span class="big">BEND</span>
    </h2>
    <div class="back-copy">
      <p>For I am the Lord your God who takes hold of your right hand and says to you, "Do not fear, I will help you." Isaiah 41:13</p>
      <p>One day you were here, Colby, the next you were at the throne of God. How I long to know what heaven is like so I can envision where you are. Are you talking to Gideon about the battles of old? Are you asking Paul about the stonings, the scales, and the shipwrecks? Or are you still just standing in awe of the God and Savior that your mother could never have come close to describing to you? How I long to stand in awe with you, praising the God who gives and takes away. Just like I told you all those times when you were here with us, "If you go first, I'll see you when I get there, my son." Love you, Mom</p>
      <p>On Friday, February 18, 2011, God did the unthinkable in our lives: He chose to take our 12-year-old son, Colby, home to heaven in a skiing accident. It is only considered the unthinkable because our plans are not God's plans and our ways are not God's ways. Follow along on my journey through the valley of the shadow of death as my Savior, Jesus Christ, leads me.</p>
    </div>
    <div class="portrait author" role="img" aria-label="Portrait photo of the author"></div>
    <p class="author-bio">Janna L. Brockwood lives on a small farm in northern Wisconsin with her husband, Dale, and their children. Experiencing the tragic death of her son has caused her to draw closer to God as He leads her down an unexpected path to know Him better.</p>
    <div class="portrait child" role="img" aria-label="Portrait photo of her son Colby"></div>
    <div class="press-mark">Still Harbor Press</div>
  </section>

  <section class="spine">
    <div class="spine-title">WHERE QUIET WATERS BEND</div>
    <div class="spine-press">Still Harbor Press</div>
  </section>

  <section class="front-cover">
    <p class="front-verse">For I am the Lord your God . who takes hold of your right hand<br>and says to you, "Do not fear, I will help you." Isaiah 41:13</p>
    <h1 class="front-title">
      <span class="big">WHERE</span>
      <span class="small">QUIET WATERS</span>
      <span class="big last">BEND</span>
    </h1>
    <p class="front-author">Janna L. Brockwood</p>
  </section>
</main>
</body>
</html>
```